Financial Research Company Brand Ad

We need a poster design for "Varnholt Analytics" 254mm(h) x 190mm (w) Our research focuses on banks, bank credit, liquidity & corporate solvency. Our believes "Get the credit & liquidity trends right & the rest follows" Please see our website for more information. www.varnholt-analytics.example

Industry/Entity Type

Bank

```html
<!DOCTYPE html>
<html lang="en">
<head>
<meta charset="utf-8">
<title>Varnholt Analytics — Credit &amp; Liquidity Research</title>
<link href="https://fonts.googleapis.com/css2?family=Roboto+Condensed:wght@300;400;600;700&display=swap" rel="stylesheet">
<style>
  :root {
    --paper: #ffffff;
    --brand-blue: #1b5795;
    --rule-grey: #8c8c8c;
    --ink: #1a1a1a;
    --tone-silver: #e4e5e5;
    --tone-grey: #c9cbcb;
    --tone-yellow: #ece39a;
    --tone-green: #9cc3a6;
    --tone-blue: #93acd2;
    --tone-red: #ec9db1;
  }
  * { margin: 0; padding: 0; box-sizing: border-box; }
  html, body { width: 898px; height: 1200px; overflow: hidden; background: var(--paper); }
  .poster {
    position: relative;
    width: 898px;
    height: 1200px;
    background: var(--paper);
    font-family: "Roboto Condensed", "Arial Narrow", sans-serif;
  }
  .rule {
    position: absolute;
    left: 0;
    width: 898px;
    height: 5px;
    background: var(--rule-grey);
  }
  .rule--top { top: 78px; }
  .rule--bottom { top: 236px; }
  .headline {
    position: absolute;
    top: 108px;
    left: 0;
    width: 898px;
    text-align: center;
    color: var(--brand-blue);
    font-weight: 700;
    font-size: 33px;
    line-height: 49px;
    letter-spacing: 0.3px;
    text-transform: uppercase;
  }
  .trend-artwork {
    position: absolute;
    top: 290px;
    left: 0;
    width: 898px;
    height: 445px;
    background: linear-gradient(180deg,
      var(--paper) 0%,
      var(--tone-silver) 14%,
      var(--tone-grey) 28%,
      var(--tone-yellow) 40%,
      var(--tone-green) 52%,
      var(--tone-blue) 66%,
      var(--tone-red) 80%,
      var(--paper) 100%);
  }
  .belief-band {
    position: absolute;
    top: 820px;
    left: 0;
    width: 898px;
    height: 138px;
    background: var(--brand-blue);
    color: var(--paper);
    display: flex;
    align-items: center;
    justify-content: center;
    text-align: center;
    font-weight: 300;
    font-size: 38px;
    line-height: 46px;
    text-transform: uppercase;
  }
  .brand {
    position: absolute;
    top: 1052px;
    left: 60px;
    display: flex;
    align-items: center;
    gap: 32px;
  }
  .brand__dot {
    width: 80px;
    height: 80px;
    border-radius: 50%;
    background: var(--brand-blue);
  }
  .brand__name {
    font-weight: 700;
    font-size: 29px;
    color: var(--ink);
  }
</style>
</head>
<body>
<main class="poster">
  <div class="rule rule--top"></div>
  <h1 class="headline">At Varnholt Analytics we focus on banks, bank<br>credit, liquidity and corporate solvency</h1>
  <div class="rule rule--bottom"></div>

  <div class="trend-artwork" role="img" aria-label="Decorative painted illustration of many coloured market trend lines rising to a sharp peak"></div>

  <section class="belief-band">
    <p>We believe if you get the credit and<br>liquidity trends right, the rest follows</p>
  </section>

  <footer class="brand">
    <span class="brand__dot"></span>
    <span class="brand__name">Varnholt-Analytics</span>
  </footer>
</main>
</body>
</html>
```